Design a business card for a hair barber [FAST TURNAROUND] [OTHER PROJECTS AVAILABLE]

I need to have this business card re-designed for a barbershop.

I want a new and eye-catching design and modern.

Please post your design in a mock-up for better presentation.

```html
<!DOCTYPE html>
<html lang="en">
<head>
<meta charset="utf-8">
<title>Ridgeline Fade Co. — Business Cards</title>
<link href="https://fonts.googleapis.com/css2?family=Open+Sans:wght@400;600;700&display=swap" rel="stylesheet">
<style>
  :root{
    --page:#e9eaec;
    --card:#ffffff;
    --ink:#2b2b2b;
    --muted:#555a60;
    --badge:#3a3a3a;
    --red:#e0262b;
    --blue:#2f5fb3;
    --pattern-a:#d9d9d9;
    --pattern-b:#f2f2f2;
    --pay-green:#2f7d3a;
    --pay-teal:#3d8a6a;
  }
  *{box-sizing:border-box;margin:0;padding:0}
  html,body{width:1200px;height:900px;overflow:hidden}
  body{background:var(--page);font-family:"Open Sans",Arial,sans-serif;color:var(--ink);position:relative}
  .card{position:absolute;left:250px;width:700px;height:400px;background:var(--card);box-shadow:0 6px 18px rgba(0,0,0,.15);overflow:hidden}
  .card--voucher{top:30px}
  .card--info{top:470px}

  /* Voucher card */
  .stripe-top{position:absolute;top:0;left:0;right:0;height:16px;
    background:repeating-linear-gradient(-45deg,var(--red) 0 18px,#fff 18px 30px,var(--blue) 30px 48px,#fff 48px 60px)}
  .stripe-right{position:absolute;top:0;right:0;bottom:0;width:16px;
    background:repeating-linear-gradient(-45deg,var(--red) 0 18px,#fff 18px 30px,var(--blue) 30px 48px,#fff 48px 60px)}
  .contact{position:absolute;top:50px;left:40px;list-style:none;font-size:14px;color:var(--muted)}
  .contact li{display:flex;align-items:center;gap:10px;margin-bottom:12px}
  .contact svg{width:16px;height:16px;fill:var(--muted)}
  .scissors-art{position:absolute;left:90px;top:170px;width:170px;height:130px;border-radius:8px;
    background:linear-gradient(135deg,#e6e6e6,#bdbdbd)}
  .discount{position:absolute;left:330px;top:150px;width:110px;height:62px;background:var(--red);color:#fff;
    border-radius:4px;text-align:center;padding-top:8px}
  .discount__value{font-size:24px;font-weight:700;line-height:1}
  .discount__value small{font-size:11px;font-weight:600}
  .discount__label{font-size:11px;font-weight:600;letter-spacing:.5px}
  .gift{position:absolute;left:460px;top:140px}
  .gift__word{font-size:62px;font-weight:700;letter-spacing:4px;line-height:1}
  .gift__word .g{color:var(--red)} .gift__word .rest{color:var(--blue)}
  .gift__sub{font-size:13px;color:var(--muted);letter-spacing:1px;margin-left:4px;line-height:1.3}
  .expiry{position:absolute;left:345px;top:250px;background:var(--red);color:#fff;font-size:13px;padding:5px 14px;border-radius:2px}
  .brand{position:absolute;left:470px;top:270px;display:flex;align-items:center;gap:8px;font-size:17px;font-weight:700;color:var(--ink)}
  .brand__dot{width:14px;height:14px;border-radius:50%;background:var(--ink)}

  /* Info card */
  .pattern{position:absolute;left:0;top:0;width:430px;height:400px;
    background:linear-gradient(135deg,var(--pattern-a),var(--pattern-b))}
  .badge{position:absolute;left:95px;top:135px;width:250px;height:110px;background:var(--badge);border-radius:30px;
    display:flex;align-items:center;justify-content:center;color:#fff;font-size:30px;letter-spacing:2px}
  .badge::after{content:"";position:absolute;inset:8px;border:2px dashed #fff;border-radius:24px}
  .social{position:absolute;left:26px;top:26px;display:flex;flex-direction:column;gap:6px;font-size:13px;font-weight:600;color:var(--ink)}
  .social span{display:flex;align-items:center;gap:6px}
  .social span::before{content:"";width:10px;height:10px;background:var(--ink)}
  .about{position:absolute;left:370px;top:40px;width:300px;font-size:13px;line-height:1.5;color:var(--muted)}
  .about h1{font-size:20px;font-weight:700;color:var(--ink);margin-bottom:6px}
  .hours{position:absolute;left:450px;top:260px;font-size:14px;color:var(--ink)}
  .pay{position:absolute;right:30px;bottom:28px;display:flex;gap:10px}
  .pay span{width:40px;height:40px;border-radius:4px}
  .pay .p1{background:var(--pay-teal)} .pay .p2{background:#fff;border:3px solid var(--ink)} .pay .p3{background:var(--pay-green)}
</style>
</head>
<body>
  <section class="card card--voucher">
    <div class="stripe-top"></div>
    <div class="stripe-right"></div>
    <ul class="contact">
      <li><svg viewBox="0 0 24 24"><path d="M6.6 10.8a15 15 0 0 0 6.6 6.6l2.2-2.2a1 1 0 0 1 1-.25 11 11 0 0 0 3.6.6 1 1 0 0 1 1 1V20a1 1 0 0 1-1 1A17 17 0 0 1 3 4a1 1 0 0 1 1-1h3.5a1 1 0 0 1 1 1c0 1.25.2 2.45.6 3.6a1 1 0 0 1-.25 1z"/></svg>555-014-2290</li>
      <li><svg viewBox="0 0 24 24"><path d="M2 5h20v14H2z M2 5l10 8 10-8" stroke="#fff" stroke-width="1.5"/></svg>hello@ridgelinefade.com</li>
      <li><svg viewBox="0 0 24 24"><path d="M12 2a7 7 0 0 0-7 7c0 5 7 13 7 13s7-8 7-13a7 7 0 0 0-7-7zm0 9.5A2.5 2.5 0 1 1 12 6.5a2.5 2.5 0 0 1 0 5z"/></svg>220 Alder Street</li>
    </ul>
    <div class="scissors-art" role="img" aria-label="Illustration of open barber scissors"></div>
    <div class="discount">
      <div class="discount__value">30%<small> off</small></div>
      <div class="discount__label">DISCOUNT</div>
    </div>
    <div class="gift">
      <div class="gift__word"><span class="g">G</span><span class="rest">IFT</span></div>
      <div class="gift__sub">VOUCHER<br>(HAIR SERVICES)</div>
    </div>
    <div class="expiry">Expiration</div>
    <div class="brand"><span class="brand__dot"></span>Ridgeline Fade Co.</div>
  </section>

  <section class="card card--info">
    <div class="pattern" role="img" aria-label="Light grey pattern of barber tools: combs, clippers, razors and brushes"></div>
    <div class="social"><span>Snapfolio</span><span>Friendwall</span></div>
    <div class="badge">BARBER SHOP</div>
    <div class="about">
      <h1>Ridgeline Fade Co.</h1>
      <p>is a family-oriented hair styling shop. We listen to our clients needs, wants and fulfill them within the business guidelines. We provide a pleasant environment for all ages and ethnicities.</p>
    </div>
    <div class="hours">(Mon-Sat) 9am-7pm</div>
    <div class="pay"><span class="p1"></span><span class="p2"></span><span class="p3"></span></div>
  </section>
</body>
</html>
```